Dog Grooming Provisions - Coat Revival Mist *

We are Moss Hollow Meadows. A city dog's country camp. We are a dog services company providing a camp experience in Upstate NY to the dogs of NYC. We are creating a hand made Coat Revival Mist for our clients (who are dogs!) for the holidays.
These labels will be used on a 4 ounce vintage style spray bottles. The design should have a vintage grooming provisions feel. We'd like to see the design be a simple, vintage style black with white, charcoal, or very dark almost black green.
The design should incorporate our varying vintage fonts, our logo with "grooming provisions" all natural & handmade, Coat Revive
Obviously this is a gift and while Coat Revive is important, our brand should be a focus. Perhaps a very simple and "elegant" bone but steer away from paws and pet cheesy! Classic, vintage and camp.

Target Market(s)

Upscale Pet Owners of NYC

Industry/Entity Type

Pet Care

Logo Text

Moss Hollow Meadows Dog Camp (Dog Camp is is for logo not necessary for label)

Font styles to use
Serif
Sans Serif
Script

Colors
9bcb3b
000000
5c5c5c

Requirements
Must have
• I am looking for a black and white or very simple design. I'd even like our logo for this use be black/white (if possible? - not sure if that can happen?)
• Our branding! Simple vintage feel.
• Grooming Provisions
• Coat Revival or Coat Revive or Coat Bright Mist
• Handmade
• All Natural
• Fonts of vintage style - varying with simple and bold (i attached some photos)
Nice to have
• **MAYBE a very Simple Bone (see drawing) - very very thin.
Should not have
• 1. PAWS or cheap looking dog related items
• 2. No bright colors - truly prefer black and white or black with intention to print on plain pulp/brown paper (attached photo)
• 3. Over designed

```html
<!DOCTYPE html>
<html lang="en">
<head>
<meta charset="utf-8">
<title>Moss Hollow Meadows – Coat Revive Label</title>
<link rel="stylesheet" href="https://fonts.googleapis.com/css2?family=Allura&family=Lato:ital,wght@0,300;0,400;0,700;1,300&family=Playball&family=Poiret+One&display=swap">
<style>
  :root {
    --ink: #1f4a3a;
    --paper: #ffffff;
    --rule: #4a4a4a;
  }
  * { margin: 0; padding: 0; box-sizing: border-box; }
  html, body {
    width: 1200px;
    height: 2336px;
    overflow: hidden;
    background: var(--paper);
  }
  h1, h2, p { font-weight: 400; }
  .label {
    position: relative;
    width: 1200px;
    height: 2336px;
    color: var(--ink);
    font-family: "Lato", sans-serif;
  }
  .label__frame {
    position: absolute;
    left: 96px;
    top: 92px;
    width: 1004px;
    height: 2143px;
    border: 2px solid var(--rule);
  }
  .brand-rule {
    position: absolute;
    top: 284px;
    height: 7px;
    background: var(--ink);
  }
  .brand-rule--left { left: 144px; width: 196px; }
  .brand-rule--right { left: 852px; width: 202px; }
  .brand-mark {
    position: absolute;
    left: 360px;
    width: 480px;
    top: 170px;
    height: 490px;
    display: flex;
    flex-direction: column;
    align-items: center;
    justify-content: center;
    gap: 28px;
  }
  .brand-mark__dot {
    width: 90px;
    height: 90px;
    border-radius: 50%;
    background: var(--ink);
  }
  .brand-mark__name {
    font-family: "Lato", sans-serif;
    font-weight: 400;
    font-size: 42px;
    color: var(--ink);
    text-align: center;
    line-height: 1.2;
  }
  .wordmark {
    position: absolute;
    left: 150px;
    right: 150px;
    top: 720px;
    text-align: center;
    white-space: nowrap;
    font-family: "Allura", cursive;
    font-weight: 400;
    font-size: 230px;
    line-height: 1.1;
  }
  .tagline {
    position: absolute;
    left: 0; right: 0;
    top: 1108px;
    text-align: center;
    font-family: "Lato", sans-serif;
    font-weight: 300;
    font-style: italic;
    font-size: 60px;
    display: flex;
    justify-content: center;
    align-items: center;
    gap: 18px;
  }
  .tagline__bone { width: 62px; height: 28px; }
  .product-name {
    position: absolute;
    left: 0; right: 0;
    top: 1295px;
    text-align: center;
    white-space: nowrap;
    font-family: "Poiret One", sans-serif;
    font-weight: 400;
    font-size: 108px;
    letter-spacing: 18px;
    padding-left: 18px;
  }
  .flourish {
    position: absolute;
    left: 150px;
    top: 1520px;
    width: 900px;
    height: 56px;
  }
  .claim {
    position: absolute;
    left: 0; right: 0;
    top: 1640px;
    text-align: center;
    white-space: nowrap;
    font-family: "Playball", cursive;
    font-size: 100px;
  }
  .established {
    position: absolute;
    left: 0; right: 0;
    top: 1935px;
    font-family: "Lato", sans-serif;
    font-weight: 400;
    font-size: 56px;
    display: flex;
    justify-content: center;
    align-items: center;
    gap: 14px;
  }
  .established__bone { width: 36px; height: 18px; }
  .volume {
    position: absolute;
    right: 162px;
    top: 2095px;
    font-family: "Lato", sans-serif;
    font-weight: 700;
    font-size: 46px;
  }
</style>
</head>
<body>
  <main class="label">
    <div class="label__frame"></div>

    <div class="brand-rule brand-rule--left"></div>
    <div class="brand-rule brand-rule--right"></div>
    <div class="brand-mark">
      <span class="brand-mark__dot"></span>
      <span class="brand-mark__name">Moss Hollow Meadows</span>
    </div>

    <h1 class="wordmark">moss hollow</h1>

    <p class="tagline">
      <span>Grooming</span>
      <svg class="tagline__bone" viewBox="0 0 62 28" aria-hidden="true">
        <path d="M12 4 a8 8 0 0 0 0 10 a8 8 0 0 0 0 10 a8 8 0 0 0 10-4 h18 a8 8 0 0 0 10 4 a8 8 0 0 0 0-10 a8 8 0 0 0 0-10 a8 8 0 0 0-10 4 h-18 a8 8 0 0 0-10-4 z" fill="none" stroke="#1f4a3a" stroke-width="2"/>
      </svg>
      <span>provisions</span>
    </p>

    <h2 class="product-name">COAT REVIVE</h2>

    <svg class="flourish" viewBox="0 0 900 56" aria-hidden="true">
      <path d="M0 44 Q120 22 260 26 Q340 28 400 16" fill="none" stroke="#1f4a3a" stroke-width="5" stroke-linecap="round"/>
      <path d="M900 44 Q780 22 640 26 Q560 28 500 16" fill="none" stroke="#1f4a3a" stroke-width="5" stroke-linecap="round"/>
      <g fill="#1f4a3a">
        <circle cx="430" cy="10" r="6"/><circle cx="430" cy="22" r="6"/>
        <circle cx="470" cy="10" r="6"/><circle cx="470" cy="22" r="6"/>
        <rect x="430" y="11" width="40" height="10"/>
      </g>
    </svg>

    <p class="claim">Handmade all natural</p>

    <p class="established">
      <svg class="established__bone" viewBox="0 0 36 18" aria-hidden="true">
        <g fill="#1f4a3a"><circle cx="5" cy="5" r="4"/><circle cx="5" cy="13" r="4"/><circle cx="31" cy="5" r="4"/><circle cx="31" cy="13" r="4"/><rect x="5" y="6" width="26" height="6"/></g>
      </svg>
      <span>est 2005</span>
      <svg class="established__bone" viewBox="0 0 36 18" aria-hidden="true">
        <g fill="#1f4a3a"><circle cx="5" cy="5" r="4"/><circle cx="5" cy="13" r="4"/><circle cx="31" cy="5" r="4"/><circle cx="31" cy="13" r="4"/><rect x="5" y="6" width="26" height="6"/></g>
      </svg>
    </p>

    <p class="volume">4 fl. oz.</p>
  </main>
</body>
</html>
```